Book Cover for Physics Book
BrightLabScience.net
Project: Book Cover for Physics Book
Book Cover for Physics Book - Education
Creative Brief
Education
High school students. Should be colorful, bright, shiny, engaging, made to stand out. Cover will also be used for Vendora e-book cover, so title should be large enough to be easily read when image size is reduced.
Templates for sizing attached. Title and author must appear on front cover as well as bound edge. Back cover leave bar code area blank (publisher will place bar code here). Quirky Otter Studios logo should appear somewhere on back cover. BrightLabScience.net logo may be used as part of the design of front or back cover, or may be skipped completely. Back cover text: Core Mechanics Primer is an easy-to-read guide to the entire Core Mechanics course, featuring more than 500 worked-out problems with full solutions and deeper understanding questions. Core Mechanics Primer covers all major topics included in the Core Mechanics course, including: kinematics, dynamics, momentum, impulse, gravity, uniform circular motion, rotation, work, energy, power, mechanical waves, sound, electrostatics, and circuits. This book is designed to assist physics students in their high school Core Mechanics courses both as a guide throughout the course as well as a review book to guide end-of-course exam preparation. Core Mechanics Primer is integrated with the BrightLabScience.net website, which includes online question and answer forums, videos, animations, and supplemental problems to help you master the essential concepts of physics.
Concepts
KMarwick KMarwick
Also, please don't think you have to use stock photos -- illustrations and creative ideas are very much appreciated as well!
Also, just to provide some ideas, the following PixelVault images would probably relate to the book fairly well: 259173804, 362810571 Other topics covered include things like amusement park rides (things that spin, roller coasters, etc.), all of which might make interesting front cover items. Lots of great designs so far, thanks for your hard work!
Topics covered in the book include: motion (kinematics) forces (dynamics) momentum, collisions, and explosions work, energy, power circular and rotational motion pendulums, springs, and swings waves and sound electricity and circuits
Looking forward to seeing what exciting and creative designs you can put forth for this new physics book! Target audience is high school students (15-17 years of age) taking physics. Sales into this target range many times are dependent on a catchy cover, so think bright, fun, and colorful for this age range.

```html
<!DOCTYPE html>
<html lang="en">
<head>
<meta charset="utf-8">
<title>Core Mechanics Primer – Cover Spread</title>
<link rel="stylesheet" href="https://fonts.googleapis.com/css2?family=Arimo:wght@400;700&family=Luckiest+Guy&display=swap">
<style>
  :root {
    --page: #ffffff;
    --orange: #f26a1b;
    --orange-deep: #e2540f;
    --ray-yellow: #ffe94a;
    --box-tan: #e6c98e;
    --ink: #111111;
    --title-blue: #7ec8f0;
    --title-line: #1a3a6b;
    --white: #ffffff;
    --art-light: #f4d9a6;
    --art-dark: #3a5a8c;
  }
  * { box-sizing: border-box; margin: 0; padding: 0; }
  html, body { width: 1200px; height: 799px; overflow: hidden; background: var(--page); }
  .spread {
    position: absolute; left: 62px; top: 58px; width: 1086px; height: 706px;
    background: radial-gradient(circle at 75% 52%, var(--ray-yellow) 0%, #ffc23a 28%, var(--orange) 58%, var(--orange-deep) 100%);
    overflow: hidden;
  }
  .sunburst { position: absolute; inset: 0; }

  /* back cover */
  .back-copy {
    position: absolute; left: 120px; top: 14px; width: 341px; height: 576px;
    background: var(--box-tan); border: 2px solid var(--ink);
    padding: 12px 12px;
    font-family: "Arimo", Arial, sans-serif; font-weight: 700;
    font-size: 14.5px; line-height: 1.16; color: var(--ink);
  }
  .publisher {
    position: absolute; left: 12px; top: 470px;
    display: flex; align-items: center; gap: 8px;
    font-family: "Arimo", Arial, sans-serif; font-weight: 700; font-size: 13px; color: var(--ink);
  }
  .publisher .dot { width: 22px; height: 22px; border-radius: 50%; background: var(--orange); }
  .barcode-area {
    position: absolute; right: 0; bottom: 0; width: 110px; height: 86px; background: var(--white);
  }
  .site-mark {
    position: absolute; left: 82px; top: 606px;
    display: flex; align-items: center; gap: 6px;
    font-family: "Arimo", Arial, sans-serif; font-weight: 700; font-size: 11px; color: var(--ink);
  }
  .site-mark .dot { width: 26px; height: 26px; border-radius: 50%; background: var(--art-dark); }

  /* spine */
  .spine-title {
    position: absolute; left: 478px; top: 40px; width: 62px; height: 520px;
    display: flex; align-items: center; justify-content: center;
  }
  .spine-title span {
    writing-mode: vertical-rl; white-space: nowrap;
    font-family: "Luckiest Guy", Impact, sans-serif; font-size: 46px; letter-spacing: 3px;
    color: var(--white); -webkit-text-stroke: 1.5px var(--ink);
  }

  /* front cover */
  .front-title { position: absolute; left: 548px; top: 10px; width: 520px; height: 215px; overflow: visible; }
  .front-title text { font-family: "Luckiest Guy", Impact, sans-serif; }
  .hero-art {
    position: absolute; left: 634px; top: 225px; width: 260px; height: 345px;
    border-radius: 46% 46% 38% 38%;
    background: radial-gradient(circle at 50% 55%, var(--art-light) 0%, #c9a56a 40%, var(--art-dark) 100%);
    opacity: .9;
  }
  .author {
    position: absolute; right: 24px; top: 582px;
    font-family: "Arimo", Arial, sans-serif; font-weight: 700; font-size: 24px; color: var(--ink);
  }
</style>
</head>
<body>
<main class="spread">
  <div class="sunburst" role="img" aria-label="Yellow sunburst rays on orange background"></div>

  <section class="back-cover">
    <div class="back-copy">
      <p>Core Mechanics Primer is an easy-to-read guide to the entire Core Mechanics course, featuring more than 500 worked-out problems with full solutions and deeper understanding questions. Core Mechanics Primer covers all major topics included in the Core Mechanics course, including: kinematics, dynamics, momentum, impulse, gravity, uniform circular motion, rotation, work, energy, power, mechanical waves, sound, electrostatics, and circuits.</p>
      <p>This book is designed to assist physics students in their high school Core Mechanics courses both as a guide throughout the course as well as a review book to guide end-of-course exam preparation.</p>
      <p>Core Mechanics Primer is integrated with the BrightLabScience.net website, which includes online question and answer forums, videos, animations, and supplemental problems to help you master the essential concepts of physics.</p>
      <div class="publisher"><span class="dot"></span>Quirky Otter Studios</div>
      <div class="barcode-area" aria-label="Reserved barcode area"></div>
    </div>
    <div class="site-mark"><span class="dot"></span>BrightLabScience.net</div>
  </section>

  <div class="spine-title"><span>CORE MECHANICS</span></div>

  <section class="front-cover">
    <svg class="front-title" viewBox="0 0 520 215" aria-label="Core Mechanics Primer">
      <defs>
        <path id="title-arc" d="M30 150 Q260 10 490 150"/>
      </defs>
      <text font-size="50" fill="var(--title-blue)" stroke="var(--title-line)" stroke-width="2" text-anchor="middle">
        <textPath href="#title-arc" startOffset="50%" textLength="440" lengthAdjust="spacingAndGlyphs">CORE MECHANICS</textPath>
      </text>
      <text x="232" y="200" font-size="46" fill="var(--title-blue)" stroke="var(--title-line)" stroke-width="2" letter-spacing="3" text-anchor="middle">PRIMER</text>
    </svg>
    <div class="hero-art" role="img" aria-label="Illustration of a cartoon scientist holding glowing energy and a spinning disc"></div>
    <p class="author">By Kai Marwick</p>
  </section>
</main>
</body>
</html>
```